Tildens Biscuit Barn Website

I need a website for a diner/restaurant that has been established in a farming, oil and industrial community for over 15 years. The website needs to be simple in design, but that should demonstrate the mastery of skills of the designer. Our diner/restaurant is family oriented, patriotic but very rustic
Fb Address is fb.me/TildensBarn

Pictures of the restaurant

https://www.filecrate-example.net/s/qk72hdw01/Tildens_05.jpg

Pictures of About us

https://www.filecrate-example.net/sh/zm40vrt88/AboutUsPhotos

Article about Tilden's
https://www.filecrate-example.net/s/wp31nbx57/TildensBiscuitBarn1.PDF
https://www.filecrate-example.net/s/hy65lcu29/TildensBiscuitBarn2.PDF

Reason: I was slow to update with information.

Reason: I am just getting feedback to the designs posted. I wasn't sure of the limited feedback was limiting designers from submitting designs. That and running a business with 25 employees open 12 hours a day, being here 2 hours prior and 2-3 hours after makes for long days.

I've increased the first place prize and also added funds to the second and third place prizes for your effort.

I just need the files in PSD, not HTML 5 as originally requested. We can handle getting the coding part.

Ill have the contest finalized by Monday. Thanks for your patience.

Target Market(s)

Cross section of adults from 18-35 & 35-55.

Industry/Entity Type

Industrial

Font styles to use
Other font styles liked:
• ff tisa web pro or garamond premier pro

Requirements
Must have
• Must be clean, look nice and not look like an afterthought.
Nice to have
• Please see the last two documents for information about our restaurant, which was featured in our local newspaper.

```html
<!DOCTYPE html>
<html lang="en">
<head>
<meta charset="utf-8">
<title>Tilden's Biscuit Barn</title>
<link href="https://fonts.googleapis.com/css2?family=EB+Garamond:wght@500;700&family=Open+Sans:wght@400;600&display=swap" rel="stylesheet">
<style>
:root{
  --artboard:#6d6e72;
  --paper:#dcd8cd;
  --paper-light:#ebe8e0;
  --brand-red:#9b1a2f;
  --brand-teal:#2f6579;
  --teal-light:#4a8196;
  --teal-dark:#1b4659;
  --panel:#e6e6e6;
  --ink-soft:#5a5a5a;
  --nav-teal:#2f6579;
}
*{margin:0;padding:0;box-sizing:border-box}
html,body{width:1200px;height:868px;overflow:hidden;background:var(--artboard)}
.page{
  position:absolute;left:165px;top:40px;width:870px;height:788px;
  background:radial-gradient(ellipse at 50% 40%,var(--paper-light) 0%,var(--paper) 75%,#cfcabd 100%);
  font-family:"EB Garamond",Georgia,serif;
}
.brand{position:absolute;left:155px;top:138px;display:flex;align-items:center;gap:8px;white-space:nowrap}
.brand-dot{width:14px;height:14px;border-radius:50%;background:var(--brand-teal)}
.brand-name{font-family:"EB Garamond",Georgia,serif;font-weight:700;font-size:30px;line-height:1;color:var(--brand-red)}
.main-nav{position:absolute;left:305px;top:188px;display:flex;align-items:center;font-weight:700;font-size:12px;letter-spacing:1.6px;white-space:nowrap}
.main-nav a{text-decoration:none;color:var(--nav-teal);padding:0 8px}
.main-nav a.is-current{color:var(--brand-red)}
.main-nav .sep{width:1px;height:15px;background:var(--nav-teal)}
.search{position:absolute;left:603px;top:187px;width:120px;height:17px;background:#fff;border:1px solid #bbb;border-radius:3px;
  font-family:"Open Sans",Arial,sans-serif;font-size:8px;line-height:9px;color:#999;padding:3px 6px;box-shadow:inset 0 1px 2px rgba(0,0,0,.15)}
.search svg{position:absolute;right:4px;top:3px}
.search::after{content:"";position:absolute;right:18px;top:2px;width:1px;height:11px;background:#888}
.social{position:absolute;right:156px;top:223px;font-family:"Open Sans",Arial,sans-serif;font-size:9px;font-weight:600;color:var(--brand-teal);white-space:nowrap}
.panel{position:absolute;background:var(--panel);border-radius:9px;box-shadow:0 10px 14px -8px rgba(0,0,0,.35)}
.panel-head{height:35px;border-radius:9px 9px 0 0;color:#fff;font-weight:700;font-size:10.5px;letter-spacing:.8px;line-height:36px;padding:0 18px;white-space:nowrap;overflow:hidden}
.hero{left:135px;top:252px;width:593px;height:286px}
.hero .panel-head{background:var(--brand-red)}
.slide{position:absolute}
.slide--side{top:94px;width:106px;height:117px;box-shadow:0 8px 10px -6px rgba(0,0,0,.4)}
.slide--left{left:40px;background:linear-gradient(135deg,#3d4d54,#8a7f6e 60%,#c9c4bc)}
.slide--right{left:434px;width:120px;background:linear-gradient(135deg,#b7a58c,#8b7a66 50%,#6e3a2c)}
.slide--center{left:145px;top:54px;width:289px;height:192px;background:linear-gradient(160deg,#dfe3e6 0%,#b9b7b1 45%,#3b3a3c 80%,#2a2a2e);box-shadow:0 10px 12px -6px rgba(0,0,0,.45)}
.arrow{position:absolute;top:149px}
.arrow--prev{left:10px}.arrow--next{left:569px}
.caption{position:absolute;left:0;right:0;top:260px;text-align:center;font-family:"Open Sans",Arial,sans-serif;font-size:9px;color:var(--ink-soft)}
.dots{position:absolute;left:537px;top:262px;display:flex;gap:4px}
.dots span{width:10px;height:10px;border-radius:50%;background:#a5a5a5}
.dots span.is-active{background:#eee;border:1px solid #888}
.order{left:134px;top:572px;width:194px;height:142px}
.order .panel-head{background:var(--brand-red);padding:0 14px}
.field{position:absolute;left:44px;width:105px;height:17px;border-radius:2px;background:linear-gradient(#fafafa,#d2d2d2);box-shadow:0 7px 7px -4px rgba(0,0,0,.3)}
.field--one{top:51px}.field--two{top:83px}
.order-notes{position:absolute;left:44px;top:116px;list-style:none;font-family:"Open Sans",Arial,sans-serif;font-size:3.6px;line-height:4.4px;color:#555;white-space:nowrap}
.order-notes li::before{content:"\25C6  ";}
.trending{left:349px;top:572px;width:379px;height:142px}
.trending .panel-head{background:linear-gradient(90deg,var(--teal-light),var(--teal-dark));text-align:right}
.thumb{position:absolute;top:54px;width:108px;height:75px}
.thumb--diner{left:21px;background:linear-gradient(135deg,#8a5a3c,#c49a6c 50%,#5e6b7a)}
.thumb--article{left:136px;background:linear-gradient(90deg,#f4f1ea 0%,#e8e3d8 55%,#e9c8a2 56%,#d8a77a)}
.thumb--dining{left:252px;background:linear-gradient(135deg,#9a6a48,#c8a27c 45%,#48576b)}
.footer{position:absolute;left:0;right:0;top:754px;text-align:center;font-weight:700;font-size:7px;letter-spacing:.3px;color:#8a857b}
</style>
</head>
<body>
<main class="page">
  <div class="brand"><span class="brand-dot"></span><span class="brand-name">Tilden's</span></div>

  <nav class="main-nav">
    <a href="#">HOME</a><span class="sep"></span>
    <a href="#" class="is-current">ABOUT US</a><span class="sep"></span>
    <a href="#">MENU</a><span class="sep"></span>
    <a href="#">GALLERY</a>
  </nav>

  <div class="search">Search
    <svg width="10" height="10" viewBox="0 0 10 10"><circle cx="4" cy="4" r="3" fill="none" stroke="#555" stroke-width="1.3"/><line x1="6.2" y1="6.2" x2="9" y2="9" stroke="#555" stroke-width="1.5"/></svg>
  </div>
  <div class="social">fb.me/TildensBarn</div>

  <section class="panel hero">
    <div class="panel-head">GET HAPPY AT TILDEN'S</div>
    <div class="slide slide--side slide--left" role="img" aria-label="Photo of two regulars seated in a diner booth"></div>
    <div class="slide slide--side slide--right" role="img" aria-label="Photo of the cook presenting an award plaque"></div>
    <div class="slide slide--center" role="img" aria-label="Photo of two guests at a diner table with breakfast plates"></div>
    <svg class="arrow arrow--prev" width="12" height="18" viewBox="0 0 12 18"><polyline points="10,2 3,9 10,16" fill="none" stroke="#777" stroke-width="1.6"/></svg>
    <svg class="arrow arrow--next" width="12" height="18" viewBox="0 0 12 18"><polyline points="2,2 9,9 2,16" fill="none" stroke="#777" stroke-width="1.6"/></svg>
    <p class="caption">Lorem ipsum dolor sit amet.</p>
    <div class="dots"><span class="is-active"></span><span></span><span></span><span></span></div>
  </section>

  <section class="panel order">
    <div class="panel-head">PLACE YOUR ORDER NOW!</div>
    <div class="field field--one"></div>
    <div class="field field--two"></div>
    <ul class="order-notes">
      <li>Fresh biscuits baked every morning since day one.</li>
      <li>Hot coffee poured all day for every guest.</li>
      <li>Call ahead and your order waits for you.</li>
      <li>Family platters ready for pickup at the counter.</li>
      <li>Open early six days a week for breakfast.</li>
    </ul>
  </section>

  <section class="panel trending">
    <div class="panel-head">TRENDING</div>
    <div class="thumb thumb--diner" role="img" aria-label="Photo of a server carrying plates in the busy diner"></div>
    <div class="thumb thumb--article" role="img" aria-label="Local newspaper article about Tilden's"></div>
    <div class="thumb thumb--dining" role="img" aria-label="Photo of the dining room full of guests"></div>
  </section>

  <p class="footer">All rights reserved. Tilden's Biscuit Barn 2014.</p>
</main>
</body>
</html>
```